Velora Aesthetica

Medical doctor providing aesthetic medicine

* Double sided card
* Logo to be on card
Other details:
* Dr. Mirela Kostvan, BSc, MBChB, CCFP
* #214-215, 27903 83 Ave, Surrey, BC, V2T 4K7
* 604-718-2943
* info@veloraclinic.ca
* www.veloraclinic.ca

Industry/Entity Type

Medical / Health & Beauty

Contact Information for Business Card

see 'Project Description'

Colors
0054AA
0677BA
7BADD7
CADEEF
E8F1F8
FFF300
FFF600
FEFA6F
FFFEC7
FFFEE8

Requirements
Must have
• Modern, high-end design

```html
<!DOCTYPE html>
<html lang="en">
<head>
<meta charset="utf-8">
<title>Velora Aesthetica — Business Card</title>
<link href="https://fonts.googleapis.com/css2?family=Montserrat:wght@400;500;600&display=swap" rel="stylesheet">
<style>
  :root {
    --backdrop: #808080;
    --card: #ffffff;
    --gold: #e0bc3e;
    --gold-deep: #c9a53a;
    --ink: #2b2b2b;
    --text: #1a1a1a;
  }
  * { margin: 0; padding: 0; box-sizing: border-box; }
  html, body { width: 1140px; height: 1200px; overflow: hidden; }
  body {
    background: var(--backdrop);
    font-family: "Montserrat", sans-serif;
    position: relative;
  }
  .card {
    position: absolute;
    left: 223px;
    width: 695px;
    height: 406px;
    background: var(--card);
    overflow: hidden;
  }
  .card--front { top: 132px; }
  .card--back { top: 661px; }

  .brand {
    position: absolute;
    transform: translateX(-50%);
    text-align: center;
    color: var(--ink);
    font-weight: 500;
    white-space: nowrap;
  }
  .brand__dot {
    display: block;
    margin: 0 auto;
    border-radius: 50%;
    background: var(--gold);
  }
  .brand__name { display: block; }
  .brand__tag { display: block; }

  .card--front .brand { left: 185px; top: 120px; }
  .card--front .brand__dot { width: 46px; height: 46px; margin-bottom: 22px; }
  .card--front .brand__name { font-size: 35px; letter-spacing: 12px; margin-right: -12px; line-height: 1; }
  .card--front .brand__tag { font-size: 12px; letter-spacing: 7px; margin-right: -7px; margin-top: 12px; }

  .card--back .brand { left: 153px; top: 148px; }
  .card--back .brand__dot { width: 34px; height: 34px; margin-bottom: 20px; }
  .card--back .brand__name { font-size: 24px; letter-spacing: 8px; margin-right: -8px; line-height: 1; }
  .card--back .brand__tag { font-size: 8px; letter-spacing: 5px; margin-right: -5px; margin-top: 8px; }

  .name-band {
    position: absolute;
    left: 299px;
    top: 74px;
    right: 0;
    height: 75px;
    background: var(--gold);
    color: #fff;
    padding: 11px 0 0 36px;
  }
  .name-band__name { font-size: 29px; font-weight: 500; line-height: 1.1; }
  .name-band__credentials { font-size: 14.5px; font-weight: 500; line-height: 1.1; margin-top: 1px; }

  .address {
    position: absolute;
    left: 301px;
    top: 188px;
    font-size: 14.5px;
    color: var(--text);
  }
  .contacts {
    position: absolute;
    left: 301px;
    top: 221px;
    list-style: none;
  }
  .contacts__item {
    display: flex;
    align-items: center;
    height: 29.7px;
    font-size: 15.5px;
    color: var(--text);
  }
  .contacts__icon {
    width: 17px;
    height: 17px;
    margin-right: 17px;
    flex: none;
  }
</style>
</head>
<body>

<section class="card card--front">
  <div class="brand">
    <span class="brand__dot"></span>
    <span class="brand__name">VELORA</span>
    <span class="brand__tag">AESTHETICA</span>
  </div>
</section>

<section class="card card--back">
  <div class="brand">
    <span class="brand__dot"></span>
    <span class="brand__name">VELORA</span>
    <span class="brand__tag">AESTHETICA</span>
  </div>

  <div class="name-band">
    <p class="name-band__name">Dr. Mirela Kostvan</p>
    <p class="name-band__credentials">BSc, MBChB, CCFP</p>
  </div>

  <p class="address">27903 83 Ave, Surrey, BC, V2T 4K7</p>

  <ul class="contacts">
    <li class="contacts__item">
      <svg class="contacts__icon" viewBox="0 0 20 20" aria-hidden="true">
        <circle cx="10" cy="10" r="10" fill="#e0bc3e"/>
        <path d="M10 4.5a3.5 3.5 0 0 0-3.5 3.5c0 2.6 3.5 7 3.5 7s3.5-4.4 3.5-7A3.5 3.5 0 0 0 10 4.5zm0 4.8a1.3 1.3 0 1 1 0-2.6 1.3 1.3 0 0 1 0 2.6z" fill="#fff"/>
      </svg>
      #214-215, 27903
    </li>
    <li class="contacts__item">
      <svg class="contacts__icon" viewBox="0 0 20 20" aria-hidden="true">
        <circle cx="10" cy="10" r="10" fill="#e0bc3e"/>
        <rect x="7" y="5" width="6" height="10" rx="1" fill="none" stroke="#fff" stroke-width="1.4"/>
        <circle cx="10" cy="13" r="0.8" fill="#fff"/>
      </svg>
      604-718-2943
    </li>
    <li class="contacts__item">
      <svg class="contacts__icon" viewBox="0 0 20 20" aria-hidden="true">
        <circle cx="10" cy="10" r="10" fill="#e0bc3e"/>
        <rect x="5" y="6.5" width="10" height="7" fill="none" stroke="#fff" stroke-width="1.3"/>
        <path d="M5 6.5l5 4 5-4" fill="none" stroke="#fff" stroke-width="1.3"/>
      </svg>
      info@veloraclinic.ca
    </li>
    <li class="contacts__item">
      <svg class="contacts__icon" viewBox="0 0 20 20" aria-hidden="true">
        <circle cx="10" cy="10" r="10" fill="#e0bc3e"/>
        <path d="M7.5 5v9l2.3-2.2 1.6 3.2 1.3-.6-1.6-3.1H14z" fill="#fff"/>
      </svg>
      www.veloraclinic.ca
    </li>
  </ul>
</section>

</body>
</html>
```